Brightmoor LINK Fiber Internet Service

Ad is for advertising fiber optic internet service in West Point, NE. Ad should convey fast internet. Pricing is: http://brightmoorlink.example/index.php/template-info/fiber-to-the-home

Promotion, free installation if ordered before September 31st. Telephone service also available.

To be used for chatterbook advertising.

Target Market(s)

New customers, TallowNet, Quillcast customers.

Industry/Entity Type

Telecommunications

Requirements
Must have
• Brightmoor logo, conform to chatterbook guidelines including 20% text rule
Nice to have
• Convey modern, fast, high tech, link to pricing, office phone number. Be able to change date for free installation if ordered by. Complement Brightmoor colors.
Should not have
• Do not use full name "Brightmoor Wireless, Inc." Only use "Brightmoor"

```html
<!DOCTYPE html>
<html lang="en">
<head>
<meta charset="utf-8">
<title>Brightmoor LINK Fiber Internet Service</title>
<link rel="stylesheet" href="https://fonts.googleapis.com/css2?family=Source+Sans+3:wght@400;700&display=swap">
<style>
  :root {
    --ink-navy: #1c2b3b;
    --brand-blue: #2b6f9a;
    --brand-blue-light: #3a86b5;
    --panel-white: #ffffff;
    --fiber-deep: #0d2f5c;
    --fiber-mid: #2d69a8;
    --fiber-glow: #ff7a2e;
    --fiber-hot: #ffe7c9;
  }
  html, body {
    margin: 0;
    padding: 0;
    overflow: hidden;
    background: #ffffff;
  }
  .ad-canvas {
    position: relative;
    width: 1200px;
    height: 628px;
    overflow: hidden;
    font-family: "Source Sans 3", "Helvetica Neue", Arial, sans-serif;
  }
  .fiber-visual {
    position: absolute;
    inset: 0;
    background:
      radial-gradient(ellipse 260px 140px at 640px 270px, var(--fiber-hot) 0%, rgba(255,200,140,0.6) 35%, rgba(255,122,46,0) 75%),
      radial-gradient(ellipse 380px 260px at 460px 230px, var(--fiber-glow) 0%, rgba(230,90,40,0.75) 40%, rgba(120,60,80,0) 80%),
      linear-gradient(100deg, var(--fiber-mid) 0%, #1f4f86 30%, #7a3a3a 45%, #3a5f95 70%, var(--fiber-deep) 100%);
  }
  .offer-panel {
    position: absolute;
    inset: 0;
    width: 1200px;
    height: 628px;
  }
  .brand-mark {
    position: absolute;
    top: 40px;
    right: 40px;
    display: flex;
    align-items: center;
    gap: 16px;
  }
  .brand-dot {
    width: 30px;
    height: 30px;
    border: 4px solid var(--brand-blue-light);
    border-radius: 50%;
    box-sizing: border-box;
  }
  .brand-name {
    font-size: 66px;
    font-weight: 700;
    letter-spacing: 1px;
    color: var(--brand-blue-light);
    text-transform: uppercase;
    line-height: 1;
  }
  .promo {
    position: absolute;
    top: 138px;
    right: 68px;
    text-align: right;
    color: var(--ink-navy);
    font-size: 23px;
    line-height: 30px;
  }
  .promo strong { font-weight: 700; }
  .promo p { margin: 0; }
  .pricing-button {
    position: absolute;
    top: 262px;
    left: 830px;
    width: 300px;
    height: 62px;
    display: flex;
    align-items: center;
    justify-content: center;
    color: #ffffff;
    font-size: 33px;
    font-weight: 700;
    text-decoration: none;
    background: var(--brand-blue);
    clip-path: polygon(0 0, 100% 0, 94% 100%, 6% 100%);
  }
  .call-block {
    position: absolute;
    top: 340px;
    left: 830px;
    width: 300px;
    text-align: center;
    color: var(--brand-blue);
    font-weight: 700;
    font-size: 34px;
    line-height: 42px;
  }
  .call-block p { margin: 0; }
</style>
</head>
<body>
  <main class="ad-canvas">
    <div class="fiber-visual" role="img" aria-label="Close-up of a fiber optic cable with glowing orange strands and streams of binary data on a blue background"></div>

    <svg class="offer-panel" viewBox="0 0 1200 628" aria-hidden="true">
      <polygon points="612,0 1200,0 1200,446 818,446" fill="var(--panel-white)"/>
      <polyline points="600,0 810,456 1200,456" fill="none" stroke="var(--brand-blue)" stroke-width="8"/>
    </svg>

    <div class="brand-mark">
      <span class="brand-dot"></span>
      <span class="brand-name">Brightmoor</span>
    </div>

    <div class="promo">
      <p><strong>Order before September 31st</strong></p>
      <p><strong>for FREE Installation</strong></p>
      <p>Telephone service also available</p>
    </div>

    <a class="pricing-button" href="http://brightmoorlink.example/index.php/template-info/fiber-to-the-home">Check Pricing</a>

    <div class="call-block">
      <p>Call Now</p>
      <p>402-555-0148</p>
    </div>
  </main>
</body>
</html>
```